Post Card Mailer for QUIK PATH PROSPECTS using new logo

We need a post card designed to send through the USA mail service that will go to new prospective clients.

The post card will introduce me and my new company and try to educate them our on company and services.

The goal is for them to call me or email me so I can have a discussion and try to sell our product.

Our product is a name list of individuals that are looking for consulting / help to determine if they qualify for USA social security benefits and then help to manage the process. We sell this name list to law firms that help these individuals.

Our services are better because we have a better less expensive way to identify people via the internet that want help. Our conversion rate is 15%, so every 100 leads a law firm buys the will obtain 15 customers / clients.

Designer on Logo took alot longer than expected. Also there were two projects that needed to combined into one. Which was done yesterday.

Target Market(s)

Law firms

Font styles to use
Serif
Sans Serif
Script

Colors

Designer to choose colors to be used in the design.

Requirements
Must have
• The size of the mailer should be about 6 by 8 inches.
• Two sides.
• Side 1: With our Logo and key messages we want to communicate.
• Side 2: A space to be used by the USA mail services in lower right, my photo and an introduction by me to our company and why they should buy from my company.
Nice to have
• Images that represent what we do, how we help, and our target market.
Should not have
• Poor taste in images that upset people

```html
<!DOCTYPE html>
<html lang="en">
<head>
<meta charset="utf-8">
<title>Quik Path Prospects – Postcard Mailer</title>
<link rel="stylesheet" href="https://fonts.googleapis.com/css2?family=Oswald:wght@400;500;600&family=Open+Sans:ital,wght@0,400;0,600;1,400&display=swap">
<style>
:root{
  --blue:#1f6fbf;
  --blue-light:#3a8fd6;
  --blue-deep:#165a9e;
  --grey:#6f7175;
  --grey-light:#d9d9d9;
  --ink:#2a2d33;
  --page:#d3d3d3;
  --white:#ffffff;
  --photo-a:#6b8a3c;
  --photo-b:#a3b86a;
}
*{box-sizing:border-box;margin:0;padding:0}
html,body{width:1200px;height:1200px;overflow:hidden}
body{background:var(--page);font-family:'Open Sans',Arial,sans-serif;color:var(--ink);position:relative}
.postcard{position:absolute;left:120px;width:960px;height:540px;background:var(--white);overflow:hidden;box-shadow:0 4px 14px rgba(0,0,0,.18)}
.postcard--front{top:40px}
.postcard--back{top:620px}

/* shared brand name */
.brand{display:flex;align-items:center;gap:10px;font-family:'Oswald',sans-serif;font-weight:600;color:var(--blue);letter-spacing:1px;line-height:1}
.brand__mark{width:16px;height:16px;background:var(--blue)}

/* front */
.front__header{position:absolute;left:0;top:0;width:100%;height:110px;display:flex;justify-content:space-between;align-items:center;padding:0 40px}
.front__header .brand{font-size:34px}
.front__headline{text-align:right;font-family:'Oswald',sans-serif}
.front__title{font-size:40px;font-weight:600;color:var(--blue);line-height:1.05}
.front__phone{font-size:22px;color:var(--grey);font-weight:400;display:flex;justify-content:flex-end;align-items:center;gap:8px}
.front__photo{position:absolute;left:0;top:110px;width:100%;height:280px;background:linear-gradient(120deg,var(--photo-a),var(--photo-b) 55%,#7f9a4c)}
.features{position:absolute;left:0;top:390px;width:100%;height:150px;display:grid;grid-template-columns:repeat(4,1fr)}
.feature{display:flex;flex-direction:column;align-items:center;justify-content:center;text-align:center;color:var(--white);padding:0 18px;background:var(--blue)}
.feature:nth-child(even){background:var(--blue-light)}
.feature svg{width:48px;height:48px;margin-bottom:10px}
.feature__title{font-family:'Oswald',sans-serif;font-weight:500;font-size:16px}
.feature__text{font-size:10.5px;line-height:1.35;margin-top:4px;opacity:.9}

/* back */
.back__shapes{position:absolute;left:0;top:0;width:960px;height:540px}
.intro__portrait{position:absolute;left:24px;top:22px;width:150px;height:134px;background:linear-gradient(160deg,#8c9299,#3c4047)}
.intro__name{position:absolute;left:24px;top:162px;width:150px;text-align:center}
.intro__name strong{display:block;font-family:'Oswald',sans-serif;font-weight:600;font-size:18px;line-height:1.3;color:var(--blue)}
.intro__name span{display:block;font-size:10.5px;line-height:1.3;color:var(--grey)}
.intro__heading{position:absolute;left:192px;top:22px;width:210px;font-family:'Oswald',sans-serif;font-weight:500;font-style:italic;font-size:18px;line-height:1.2;color:var(--blue)}
.intro__points{list-style:none;position:absolute;font-size:11.5px;line-height:1.4;font-style:italic}
.intro__points li{position:relative;padding-left:18px;margin-bottom:8px}
.intro__points li::before{content:"\2192";position:absolute;left:0;top:-1px;color:var(--blue);font-style:normal;font-weight:600}
.intro__points--side{left:192px;top:96px;width:215px}
.intro__points--wide{left:24px;top:232px;width:395px}
.intro__cta{position:absolute;left:24px;top:336px;width:400px;font-family:'Oswald',sans-serif;font-weight:500;font-style:italic;font-size:19px;line-height:1.2;color:var(--blue)}
.trial{position:absolute;left:24px;top:420px;color:var(--white)}
.trial h3{font-family:'Oswald',sans-serif;font-weight:500;font-size:20px;margin-bottom:6px}
.trial ul{list-style:none;font-style:italic;font-size:13px;line-height:1.5}
.trial li::before{content:"\2713  ";font-style:normal}
.mail__brand{position:absolute;left:560px;top:44px}
.mail__brand .brand{font-size:34px}
.mail__banner{position:absolute;left:520px;top:112px;width:410px;height:58px;background:var(--blue);color:var(--white);font-family:'Oswald',sans-serif;font-size:14px;line-height:1.3;display:flex;align-items:center;justify-content:center;text-align:center;padding:0 16px}
.mail__return{position:absolute;left:530px;top:222px;font-size:11px;line-height:1.55}
.mail__return p{display:flex;align-items:center;gap:6px}
.mail__stamp{position:absolute;right:30px;top:206px;width:70px;height:80px;background:var(--grey-light)}
.mail__line{position:absolute;left:560px;width:370px;height:2px;background:var(--ink)}
</style>
</head>
<body>

<section class="postcard postcard--front" aria-label="Postcard front">
  <header class="front__header">
    <div class="brand"><span class="brand__mark"></span>QUIK PATH PROSPECTS</div>
    <div class="front__headline">
      <h1 class="front__title">Helping Disabled People</h1>
      <p class="front__phone">
        <svg width="12" height="16" viewBox="0 0 12 16" aria-hidden="true"><rect x="1" y="1" width="10" height="14" rx="2" fill="none" stroke="currentColor" stroke-width="1.6"/><circle cx="6" cy="12" r="1" fill="currentColor"/></svg>
        555-014-2290
      </p>
    </div>
  </header>
  <div class="front__photo" role="img" aria-label="Photo: a smiling grandfather in a wheelchair in a sunny park, a girl running to hug him and a woman pushing the chair"></div>
  <div class="features">
    <div class="feature">
      <svg viewBox="0 0 48 48" aria-hidden="true"><path d="M6 26 L26 6 H42 V22 L22 42 Z" fill="none" stroke="#fff" stroke-width="3" stroke-linejoin="round"/><circle cx="34" cy="14" r="3" fill="#fff"/></svg>
      <div class="feature__title">Best Leads, Best Price</div>
      <div class="feature__text">Low cost per lead with more clients for your firm. Volume pricing available.</div>
    </div>
    <div class="feature">
      <svg viewBox="0 0 48 48" aria-hidden="true"><polygon points="24,3 28,9 35,7 35,14 42,17 38,23 42,29 35,32 35,39 28,37 24,43 20,37 13,39 13,32 6,29 10,23 6,17 13,14 13,7 20,9" fill="#fff"/></svg>
      <div class="feature__title">High Volume, Quality Leads</div>
      <div class="feature__text">15% of our leads become clients. Proven online search methods.</div>
    </div>
    <div class="feature">
      <svg viewBox="0 0 48 48" aria-hidden="true"><rect x="4" y="20" width="9" height="22" fill="#fff"/><path d="M16 20 L24 6 C28 6 29 9 28 13 L27 18 H40 C43 18 44 21 43 24 L39 39 C38 41 37 42 35 42 H16 Z" fill="#fff"/></svg>
      <div class="feature__title">Trusted Partner</div>
      <div class="feature__text">Reliable, responsive, helpful. Deep business and process expertise.</div>
    </div>
    <div class="feature">
      <svg viewBox="0 0 48 48" aria-hidden="true"><polygon points="24,3 30,18 46,18 33,28 38,44 24,34 10,44 15,28 2,18 18,18" fill="#fff"/></svg>
      <div class="feature__title">EZ to use</div>
      <div class="feature__text">Simple ordering and fast delivery straight to your intake team.</div>
    </div>
  </div>
</section>

<section class="postcard postcard--back" aria-label="Postcard back">
  <svg class="back__shapes" viewBox="0 0 960 540" aria-hidden="true">
    <polygon points="0,410 434,410 410,540 0,540" fill="var(--grey)"/>
    <polygon points="410,0 446,0 496,270 446,540 410,540 460,270" fill="var(--blue)"/>
  </svg>

  <div class="intro__portrait" role="img" aria-label="Portrait photo of the company president"></div>
  <div class="intro__name"><strong>Marcus Delane</strong><span>President, Quik Path Prospects</span></div>
  <h2 class="intro__heading">I want to personally introduce our company to you!</h2>
  <ul class="intro__points intro__points--side">
    <li>My team has 30 years of cumulative SSD experience.</li>
    <li>We have proven technology that delivers the best leads.</li>
    <li>The timing is right for a new competitor in this industry.</li>
  </ul>
  <ul class="intro__points intro__points--wide">
    <li>I had to come out of retirement after 30 years with Northfield Industrial; the opportunity is just that great. I love building businesses and partnering with great customers!</li>
    <li>Our business, industry &amp; technical acumen is unrivaled, and we can do it at a cost that no others can.</li>
  </ul>
  <p class="intro__cta">Let's work together to bring Social Security Disability benefits to those in need and deserving!</p>
  <div class="trial">
    <h3>Test our Leads</h3>
    <ul>
      <li>Start at 250 or 500 Leads.</li>
      <li>Grow to 1,000 … 3,000 or even 10,000!</li>
      <li>We give the right support to your growth.</li>
    </ul>
  </div>

  <div class="mail__brand"><div class="brand"><span class="brand__mark"></span>QUIK PATH PROSPECTS</div></div>
  <div class="mail__banner">Best Leads … Best Price with High Volume &amp; Quality capacity — Leads from a Trusted Partner that is EZ to use</div>
  <div class="mail__return">
    <p>Marcus Delane, President, Quik Path Prospects</p>
    <p>4410 Harbor Mill Road, Suite 210</p>
    <p>Dayton, OH 45400</p>
    <p><svg width="9" height="12" viewBox="0 0 12 16" aria-hidden="true"><rect x="1" y="1" width="10" height="14" rx="2" fill="none" stroke="currentColor" stroke-width="1.6"/></svg>555-014-2290</p>
    <p><svg width="11" height="9" viewBox="0 0 14 10" aria-hidden="true"><rect x="0.8" y="0.8" width="12.4" height="8.4" fill="none" stroke="currentColor" stroke-width="1.4"/><path d="M1 1 L7 6 L13 1" fill="none" stroke="currentColor" stroke-width="1.4"/></svg>marcus@quikpathprospects.com</p>
  </div>
  <div class="mail__stamp"></div>
  <div class="mail__line" style="top:380px"></div>
  <div class="mail__line" style="top:430px"></div>
  <div class="mail__line" style="top:480px"></div>
</section>

</body>
</html>
```